Law Firm St. Patrick's Day Party

Two different law firm's joining to have a St. Patrick's Day party. Invitees will include other lawyers, clients and friends. This is intended to be more of a causal event. So we are looking for an invite that is fun but not cheesy.

The invite will be a two sided "post card." One side should be the details of event and design. The opposite side should be our firm logos (see uploads) with an area on the right side for postage and mailing address. We will be providing live music, food and drinks. Also...the NVBL Basketball Tournaments will playing the same day...some sort of reference that we Will have TVs to watch the Basketball games is needed too.

Target Market(s)

Fun professional crowd

Industry/Entity Type

Law Firm

Font styles to use
Serif
Decorative
Script

Requirements
Must have
• time, date and where...food, drinks TVs (NVBL games)
• Essential Information: Friday, March 17th. The party will start at 2:00 p.m. and run until "Whenever." The location of the Party is 2846 Birch Lane, Kansas City, Missouri 64108.
Nice to have
• something festive for St. Pat's day

```html
<!DOCTYPE html>
<html lang="en">
<head>
<meta charset="utf-8">
<title>Law Firm's St. Patrick's Day Party – Postcard</title>
<link href="https://fonts.googleapis.com/css2?family=Berkshire+Swash&family=Crimson+Text:ital,wght@0,400;0,700;1,400;1,700&display=swap" rel="stylesheet">
<style>
  :root{
    --green:#0f9a4a;
    --green-dark:#0b7d3b;
    --green-pale:#d9efdf;
    --gold:#f2a93b;
    --ink:#3a3a3a;
    --stripe:#1f8f4a;
    --paper:#ffffff;
    --line:#6fbf8a;
  }
  *{box-sizing:border-box;margin:0;padding:0}
  html,body{width:1200px;height:463px;overflow:hidden;background:var(--paper)}
  body{position:relative;font-family:"Crimson Text",Georgia,serif;color:var(--ink)}

  .panel{
    position:absolute;top:0;height:463px;
    background:repeating-linear-gradient(135deg,var(--paper) 0 10px,var(--stripe) 10px 12px,var(--paper) 12px 22px);
  }
  .panel--back{left:0;width:596px}
  .panel--front{left:612px;width:588px}

  .card{
    position:absolute;top:36px;height:376px;background:var(--paper);
    box-shadow:3px 4px 8px rgba(0,0,0,.35);
  }
  .panel--back .card{left:45px;width:537px}
  .panel--front .card{left:15px;width:545px}

  /* back side */
  .firm-names{position:absolute;left:16px;top:24px;display:flex;gap:22px;align-items:center}
  .firm-name{display:flex;align-items:center;gap:6px;font-size:14px;color:var(--ink);line-height:1.05}
  .firm-name__mark{width:18px;height:18px;background:var(--ink)}
  .firm-name--second .firm-name__mark{background:#1e4fa0;border-radius:50%}
  .stamp-box{position:absolute;left:436px;top:37px;width:64px;height:60px;border:1.5px solid var(--green)}
  .address-lines{position:absolute;left:246px;top:186px;width:254px}
  .address-lines span{display:block;height:33px;border-bottom:1px solid var(--line)}
  .greeting-art{position:absolute;left:40px;top:138px;width:164px;height:170px;background:radial-gradient(ellipse at center,#6cc48b 0%,var(--green) 70%);border-radius:8px}

  /* front side */
  .art{position:absolute}
  .art--hat-left{left:16px;top:12px;width:85px;height:91px;background:linear-gradient(var(--gold) 0 20%,var(--green) 20%);border-radius:6px}
  .art--hat-right{left:444px;top:12px;width:88px;height:91px;background:linear-gradient(var(--gold) 0 20%,var(--green) 20%);border-radius:6px}
  .art--clovers-left{left:18px;top:130px;width:80px;height:140px;background:var(--green-pale);border-radius:40px}
  .art--clovers-right{left:448px;top:130px;width:84px;height:140px;background:var(--green-pale);border-radius:40px}
  .art--pot-left{left:12px;top:293px;width:84px;height:76px;background:linear-gradient(var(--gold) 0 22%,var(--green) 22%);border-radius:30px 30px 14px 14px}
  .art--mug-left{left:96px;top:318px;width:48px;height:52px;background:linear-gradient(#fff3c9 0 22%,var(--gold) 22%);border-radius:4px}
  .art--mug-right{left:396px;top:318px;width:48px;height:52px;background:linear-gradient(#fff3c9 0 22%,var(--gold) 22%);border-radius:4px}
  .art--pot-right{left:448px;top:293px;width:84px;height:76px;background:linear-gradient(var(--gold) 0 22%,var(--green) 22%);border-radius:30px 30px 14px 14px}

  .invite{position:absolute;left:0;width:545px;text-align:center}
  .invite__kicker{top:34px;font-size:21px}
  .invite__title{top:60px;font-family:"Berkshire Swash","Crimson Text",cursive;font-size:31px;color:var(--green)}
  .invite__line{font-style:italic;font-size:17px;line-height:22px}
  .invite__music{top:105px}
  .invite__games{top:143px}
  .invite__games strong{color:var(--green)}
  .invite__tvs{top:207px}
  .divider{position:absolute;left:107px;width:297px;border-top:1.5px dotted #9a9a9a}
  .divider--one{top:137px}
  .divider--two{top:200px}

  .banner{position:absolute;left:97px;top:258px}
  .banner__text{position:absolute;left:97px;top:262px;width:334px;text-align:center;color:#fff;font-style:italic;font-size:15px;line-height:19px}
  .venue{position:absolute;left:0;top:318px;width:545px;text-align:center;font-weight:700;font-size:18px;line-height:24px}
</style>
</head>
<body>
  <section class="panel panel--back">
    <div class="card card--back">
      <div class="firm-names">
        <div class="firm-name"><span class="firm-name__mark"></span>Harlow &amp; Finch</div>
        <div class="firm-name firm-name--second"><span class="firm-name__mark"></span>Merrit Lowe &amp; Dane, LLC</div>
      </div>
      <div class="stamp-box"></div>
      <div class="greeting-art" role="img" aria-label="Hand lettered Happy St. Patrick's Day greeting with shamrocks"></div>
      <div class="address-lines"><span></span><span></span><span></span><span></span><span></span><span></span></div>
    </div>
  </section>

  <section class="panel panel--front">
    <div class="card card--front">
      <div class="art art--hat-left" role="img" aria-label="Green leprechaun hat with shamrock"></div>
      <div class="art art--hat-right" role="img" aria-label="Green leprechaun hat with shamrock"></div>
      <div class="art art--clovers-left" role="img" aria-label="Faint scattered shamrocks"></div>
      <div class="art art--clovers-right" role="img" aria-label="Faint scattered shamrocks"></div>

      <p class="invite invite__kicker">Law Firm's</p>
      <h1 class="invite invite__title">St. Patrick's Day Party</h1>
      <p class="invite invite__line invite__music">Live Music, Food and Drinks</p>
      <div class="divider divider--one"></div>
      <p class="invite invite__line invite__games"><strong>NVBL Basketball Tournaments</strong><br>will playing the same day</p>
      <div class="divider divider--two"></div>
      <p class="invite invite__line invite__tvs">We Will have TVs to watch the<br>Basketball games is needed too</p>

      <svg class="banner" width="334" height="47" viewBox="0 0 334 47" aria-hidden="true">
        <path d="M10 0 H324 Q334 0 334 10 V20 Q334 32 322 34 Q167 52 12 34 Q0 32 0 20 V10 Q0 0 10 0 Z" fill="var(--green)"/>
      </svg>
      <p class="banner__text">Friday, March 17th.<br>The party will start at 2:00 p.m.</p>

      <div class="art art--pot-left" role="img" aria-label="Pot of gold coins"></div>
      <div class="art art--mug-left" role="img" aria-label="Mug of beer"></div>
      <p class="venue">2846 Birch Lane, Kansas City,<br>Missouri 64108.</p>
      <div class="art art--mug-right" role="img" aria-label="Mug of beer"></div>
      <div class="art art--pot-right" role="img" aria-label="Pot of gold coins"></div>
    </div>
  </section>
</body>
</html>
```